Digital Marketing Online Shop Needs a Home Page Web Design

Here is some background on the new home page and the message we want to relay to people visiting our site.
The new site design will be very similar to the following sites
http://trellisoft.com/
https://quillhaven.com/
http://brightmarrow.io/
http://sketchotter.com/
http://clipharbor.com/
We are a small marketing agency of 3 and we have built up and impressive contact list of partners over the last 16 years to help our customers take their digital marketing to the next level.
The four core areas of products we will be promoting and selling through our online shop are the following :
Web design
Content marketing
Graphic design
Coaching
We operate our agency in a new way, not the old school way so our customers can receive on-demand marketing.
We plan to have an online shop so visitors can purchase some of our services, very similar to how Quill Haven and Sketch Otter offer their services.
In the end, we want the same call to action layout as Trellisoft, Quill Haven and Sketch Otter, however, since we are an agency we would like to blend in Bright Marrow's layout.
We want the customer to either contact us about our services or purchase one of the services from our shop.
We are trying to make the whole digital marketing experience more transactional like retail and not so traditional servicey. :-)
It is from our years of experience and finding the right partners that allows us to offer this type of solution to businesses in the Maritime Provinces (New Brunswick, Nova Scotia, Prince Edward Island, Canada).
Also, because we are offering more of an on-demand/self serve option and we have lower overhead, we hope to pass along great pricing to our customers for their marketing needs. We really want this offer to expand outside of our local market in Saint John, New Brunswick.
I would also like to have a call to action written for a hero image at the top of the page, like the Trellisoft site.
After that I would like the content to flow through similar to Quill Haven & Trellisoft. But mix in some of the agency like content you see with Clipharbor, Bright Marrow.
I have also included the first draft of the content for our home page.
Menu Items will be About, How We Work, Learn, Shop, Contact
Please let me know if you need anything else.
Target Market(s)
Small businesses, 1-10 person companies with up to 5 million in revenue. Mostly service companies, but some retail.
Industry/Entity Type
Marketing
Number of Pages Required
1 page

```html
<!DOCTYPE html>
<html lang="en">
<head>
<meta charset="utf-8">
<title>Tidewell Solutions — Home</title>
<link rel="stylesheet" href="https://fonts.googleapis.com/css2?family=Source+Sans+3:wght@200;300;400;600;700;900&display=swap">
<style>
  :root{
    --nav-bg:#1c2024;
    --nav-text:#b9bcc0;
    --hero-deep:#0b1622;
    --hero-mid:#1a3048;
    --brand-blue:#1c5bb5;
    --bright-blue:#2d7fe0;
    --green:#5bb52a;
    --section-grey:#f1f1f1;
    --text-grey:#8a8a8a;
    --text-dark:#3b3b3b;
    --white:#ffffff;
    --footer-bg:#2a2a2a;
    --footer-base:#202020;
    --footer-head:#7d7d7d;
    --footer-link:#4d4d4d;
    --font:"Source Sans 3","Source Sans Pro",Arial,sans-serif;
  }
  *{box-sizing:border-box;margin:0;padding:0}
  html,body{width:1200px;height:2571px;overflow:hidden}
  body{font-family:var(--font);background:var(--white);position:relative;color:var(--text-dark)}
  .abs{position:absolute}

  /* NAV */
  .site-nav{position:absolute;left:0;top:0;width:1200px;height:60px;background:var(--nav-bg);z-index:2}
  .brand{position:absolute;left:40px;top:15px;display:flex;align-items:center;gap:10px}
  .brand-dot{width:30px;height:30px;border-radius:50%;background:var(--white)}
  .brand-name{font-size:24px;font-weight:700;color:var(--white);letter-spacing:.2px}
  .menu{position:absolute;left:492px;top:0;height:60px;display:flex;align-items:center;gap:42px;list-style:none}
  .menu li{font-size:16px;font-weight:700;color:var(--nav-text);text-transform:uppercase;letter-spacing:.2px}
  .nav-icon{position:absolute;top:19px}

  /* HERO */
  .hero{position:absolute;left:0;top:60px;width:1200px;height:598px;
    background:radial-gradient(ellipse at 60% 30%,var(--hero-mid) 0%,var(--hero-deep) 70%)}
  .hero-title{position:absolute;left:106px;top:130px;color:var(--white);font-weight:900;line-height:.92;letter-spacing:-1px}
  .hero-title .line{display:block;font-size:48px}
  .hero-title .accent{display:block;font-size:70px;color:var(--bright-blue);letter-spacing:-1.5px}
  .hero-copy{position:absolute;left:108px;top:296px;width:420px;font-size:19px;line-height:20.5px;color:#d7dde4}
  .btn{position:absolute;display:flex;align-items:center;justify-content:center;font-weight:700;font-size:20px;text-transform:uppercase;border-radius:3px}
  .btn-outline-light{border:2px solid var(--white);color:var(--white)}
  .hero-devices{position:absolute;left:552px;top:140px;width:585px;height:307px;border-radius:10px;
    background:linear-gradient(160deg,#3b4e5f 0%,#6d7f84 45%,#2a3a44 100%)}
  .slider-dots{position:absolute;left:543px;top:560px;display:flex;gap:7px}
  .slider-dots span{width:11px;height:11px;border-radius:50%;background:#c9ccd0}
  .slider-dots span.active{background:var(--bright-blue)}

  /* SERVICES */
  .services{position:absolute;left:0;top:658px;width:1200px;height:813px;background:var(--section-grey)}
  .section-title{position:absolute;left:0;width:1200px;text-align:center;top:35px;font-size:56px;font-weight:700;color:var(--brand-blue);letter-spacing:-1px}
  .title-rule{position:absolute;left:566px;top:104px;width:70px;height:2px;background:var(--text-dark)}
  .section-sub{position:absolute;left:0;width:1200px;text-align:center;top:124px;font-size:21px;color:var(--text-grey)}
  .tabs{position:absolute;top:200px;left:0;width:1200px;height:45px}
  .tab{position:absolute;top:0;font-size:17px;font-weight:700;color:var(--text-grey);text-transform:uppercase;transform:translateX(-50%);white-space:nowrap}
  .tab.active{color:var(--brand-blue)}
  .tab-bar{position:absolute;left:135px;top:39px;width:175px;height:5px;background:var(--brand-blue)}
  .collage{position:absolute;left:0;top:293px;width:497px;height:463px}
  .collage-label{position:absolute;left:255px;top:467px;width:120px;text-align:center;color:var(--white);font-size:32px;font-weight:900;line-height:34px;letter-spacing:-.5px}
  .offer-head{position:absolute;left:578px;top:318px;color:var(--green);font-size:50px;line-height:46px;letter-spacing:-.5px}
  .offer-head .thin{display:block;font-weight:300}
  .offer-head .bold{display:block;font-weight:700}
  .offer-rule{position:absolute;left:578px;top:436px;width:52px;height:2px;background:var(--text-dark)}
  .offer-copy{position:absolute;left:578px;width:500px;font-size:19px;line-height:20.5px;color:var(--text-grey)}
  .offer-copy strong{color:#6a6a6a;font-weight:700}
  .btn-outline-green{border:2px solid var(--green);color:var(--green);background:var(--white)}

  /* FEATURES */
  .features{position:absolute;left:0;top:1471px;width:1200px;height:309px;background:var(--white)}
  .feature{position:absolute;top:63px;width:260px;text-align:center;transform:translateX(-50%)}
  .feature svg{display:block;margin:0 auto;height:70px}
  .feature h3{margin-top:30px;font-size:23px;font-weight:700;color:var(--text-dark);text-transform:uppercase}
  .feature p{margin-top:4px;font-size:18px;line-height:19.5px;color:var(--text-grey)}

  /* CTA */
  .cta{position:absolute;left:0;top:1780px;width:1200px;height:560px;
    background:linear-gradient(110deg,#1d58a6 0%,#2f6db4 45%,#3d78b8 100%)}
  .cta-head{position:absolute;left:40px;top:52px;color:var(--white);font-size:56px;line-height:52px;letter-spacing:-1.5px}
  .cta-head .thin{display:block;font-weight:200}
  .cta-head .bold{display:block;font-weight:700}
  .cta-rule{position:absolute;left:40px;top:182px;width:52px;height:2px;background:var(--white)}
  .cta-copy{position:absolute;left:40px;top:204px;width:570px;font-size:20.5px;line-height:24.8px;color:var(--white)}
  .btn-fill-light{background:var(--white);color:var(--brand-blue)}

  /* FOOTER */
  .footer{position:absolute;left:0;top:2340px;width:1200px;height:163px;background:var(--footer-bg)}
  .f-col{position:absolute;top:32px;font-size:15px;line-height:17.5px;color:var(--footer-link)}
  .f-col h4{font-size:15px;font-weight:700;color:var(--footer-head);text-transform:uppercase;line-height:17.5px}
  .f-col .sub{font-weight:700;color:var(--footer-head);text-transform:uppercase}
  .f-divider{position:absolute;top:24px;width:1px;height:118px;background:#3e3e3e}
  .social{display:grid;grid-template-columns:22px 22px;gap:14px 22px;margin-top:12px}
  .social span{width:22px;height:22px;border-radius:50%;background:#8a8a8a}
  .to-top{position:absolute;left:1109px;top:58px;width:52px;height:52px;border-radius:50%;background:var(--white)}
  .footer-base{position:absolute;left:0;top:2503px;width:1200px;height:68px;background:var(--footer-base);font-size:14px;color:#555}
  .footer-base .copy{position:absolute;left:41px;top:25px}
  .footer-base .legal{position:absolute;right:40px;top:25px}
</style>
</head>
<body>

<header class="site-nav">
  <div class="brand"><span class="brand-dot"></span><span class="brand-name">Tidewell Solutions</span></div>
  <ul class="menu">
    <li>About Us</li><li>How We Work</li><li>Learn</li><li>Shop</li><li>Contact Us</li>
  </ul>
  <svg class="nav-icon" style="left:1078px" width="22" height="22" viewBox="0 0 22 22" aria-label="Search">
    <circle cx="9" cy="9" r="6.5" fill="none" stroke="var(--nav-text)" stroke-width="2.4"/>
    <line x1="14" y1="14" x2="20" y2="20" stroke="var(--nav-text)" stroke-width="2.6" stroke-linecap="round"/>
  </svg>
  <svg class="nav-icon" style="left:1138px" width="24" height="22" viewBox="0 0 24 22" aria-label="Cart">
    <path d="M1 2h4l3 12h12l2-9H6" fill="none" stroke="var(--nav-text)" stroke-width="2.2" stroke-linejoin="round"/>
    <circle cx="9" cy="18.5" r="1.8" fill="var(--nav-text)"/><circle cx="18" cy="18.5" r="1.8" fill="var(--nav-text)"/>
  </svg>
</header>

<section class="hero" role="img" aria-label="Night sky with stars over a dark landscape">
  <svg class="abs" style="left:40px;top:240px" width="40" height="120" viewBox="0 0 40 120" aria-label="Previous slide">
    <polyline points="36,2 4,60 36,118" fill="none" stroke="#c8ced6" stroke-width="2"/>
  </svg>
  <svg class="abs" style="left:1120px;top:240px" width="40" height="120" viewBox="0 0 40 120" aria-label="Next slide">
    <polyline points="4,2 36,60 4,118" fill="none" stroke="#c8ced6" stroke-width="2"/>
  </svg>
  <h1 class="hero-title">
    <span class="line">YOUR BEAUTY AND</span>
    <span class="accent">RESPONSIVE</span>
    <span class="line">DESIGN IS HERE!</span>
  </h1>
  <p class="hero-copy">Discover quality and beautiful website layouts, built by professionals that focus in provide you the most modern and efficient work, in order to make grow up your business and help you to reach the best results as possible.</p>
  <div class="btn btn-outline-light" style="left:110px;top:429px;width:166px;height:44px">Learn More</div>
  <div class="hero-devices" role="img" aria-label="Phone, tablet and laptop showing the responsive website"></div>
  <div class="slider-dots"><span></span><span class="active"></span><span></span><span></span><span></span><span></span></div>
</section>

<section class="services">
  <h2 class="section-title">Our Services</h2>
  <div class="title-rule"></div>
  <p class="section-sub">Find the right service for you to make grow up your business.</p>
  <nav class="tabs">
    <span class="tab active" style="left:223px">Web Design</span>
    <span class="tab" style="left:477px">Content Marketing</span>
    <span class="tab" style="left:754px">Graphic Design</span>
    <span class="tab" style="left:986px">Coaching</span>
    <div class="tab-bar"></div>
  </nav>

  <svg class="collage" viewBox="0 0 497 463" role="img" aria-label="Hexagon collage of web design workspace photos: desk with computer, tablet and code">
    <polygon points="105,0 168,0 200,55 168,110 105,110 73,55" fill="#5d7a58"/>
    <polygon points="0,52 48,52 70,90 48,128 0,128" fill="#6f6f6f"/>
    <polygon points="0,118 70,118 105,178 70,238 0,238" fill="#6f8a62"/>
    <polygon points="0,205 20,205 38,280 20,355 0,355" fill="#5c5c5c"/>
    <polygon points="95,256 135,256 155,290 135,324 95,324 75,290" fill="#d0d0d0"/>
    <polygon points="150,300 168,300 178,317 168,334 150,334 140,317" fill="#8e8e8e"/>
    <polygon points="0,335 110,335 145,400 110,463 0,463" fill="#2e4030"/>
    <polygon points="190,65 405,65 497,230 405,395 190,395 135,230" fill="#76705a"/>
  </svg>
  <div class="collage-label">WEB<br>DESIGN</div>

  <h2 class="offer-head"><span class="thin">Mark your</span><span class="bold">presence online</span></h2>
  <div class="offer-rule"></div>
  <p class="offer-copy" style="top:465px">Find the latest creative tools in only one place, and have your next website just the way you think. From an e-commerce till a news website, we can help you to improve you business comunication, in order to reach more clients and the results that you long for.</p>
  <p class="offer-copy" style="top:593px"><strong>Want you to order this service, or know more about it?</strong> You can contact us by phone or email to order this service or know more info. IBut, if you prefer, you can do it all totaly online, starting by clicking on the button below:</p>
  <div class="btn btn-outline-green" style="left:578px;top:701px;width:168px;height:45px">Get Started</div>
</section>

<section class="features">
  <div class="feature" style="left:189px">
    <svg viewBox="0 0 64 64" width="70" aria-hidden="true"><polygon points="32,4 40,24 62,25 45,39 51,60 32,48 13,60 19,39 2,25 24,24" fill="none" stroke="#777" stroke-width="1.6" stroke-linejoin="round"/></svg>
    <h3>Rating</h3><p>Lorem ipsum dolor sit amet, consectetur adipiscing elit.</p>
  </div>
  <div class="feature" style="left:463px">
    <svg viewBox="0 0 64 64" width="70" aria-hidden="true"><path d="M8 6v50h52" fill="none" stroke="#777" stroke-width="1.6"/><polyline points="14,44 26,30 36,38 52,22" fill="none" stroke="#777" stroke-width="1.6"/><path d="M18 56v4M28 56v4M38 56v4M48 56v4" stroke="#777" stroke-width="1.4"/></svg>
    <h3>Numbers</h3><p>Nam venenatis dapibus arcu, a suscipit elit interdum eu.</p>
  </div>
  <div class="feature" style="left:739px">
    <svg viewBox="0 0 64 64" width="70" aria-hidden="true"><circle cx="32" cy="35" r="22" fill="none" stroke="#777" stroke-width="1.6"/><path d="M6 15a9 9 0 0 1 14-8M58 15a9 9 0 0 0-14-8" fill="none" stroke="#777" stroke-width="1.6"/><polyline points="32,20 32,35 42,41" fill="none" stroke="#777" stroke-width="1.6"/><path d="M16 54l-5 6M48 54l5 6" stroke="#777" stroke-width="1.6"/></svg>
    <h3>Efficiency</h3><p>Aliquam fermentum urna convallis lectus ornare, sed pellentesque odio porta.</p>
  </div>
  <div class="feature" style="left:1010px">
    <svg viewBox="0 0 64 64" width="70" aria-hidden="true"><path d="M22 44c0-8-10-12-10-23a20 20 0 0 1 40 0c0 11-10 15-10 23z" fill="none" stroke="#777" stroke-width="1.6"/><path d="M24 50h16M25 55h14M28 60h8" stroke="#777" stroke-width="1.6"/><path d="M29 44V28l3 4 3-4v16" fill="none" stroke="#777" stroke-width="1.4"/></svg>
    <h3>Creativity</h3><p>Fusce erat mauris, cursus sed metus sit amet, efficitur dignissim lacus.</p>
  </div>
</section>

<section class="cta" role="img" aria-label="Hiker walking along a green mountain ridge, tinted blue">
  <h2 class="cta-head"><span class="thin">We will help you get to</span><span class="bold">where you want to be!</span></h2>
  <div class="cta-rule"></div>
  <p class="cta-copy">Lorem ipsum dolor sit amet, consectetur adipiscing elit. Proin id quam laoreet, gravida ligula quis, rhoncus metus. Cras consectetur rhoncus molestie. Proin enim mi, hendrerit sit amet libero ut, placerat fermentum diam. Donec aliquam a lacus quis pharetra. Nullam vehicula elit ac lobortis dignissim. Pellentesque viverra massa eget tempus porttitor. Nunc molestie eget libero at finibus. Morbi mauris lectus, tincidunt quis ligula at, porttitor suscipit quam.</p>
  <div class="btn btn-outline-light" style="left:40px;top:452px;width:167px;height:45px">Get Started</div>
  <div class="btn btn-fill-light" style="left:231px;top:452px;width:167px;height:45px">Learn More</div>
</section>

<footer class="footer">
  <div class="f-col" style="left:41px"><h4>Tidewell Solutions</h4>Lorem Ipsum Dolor, 555 - Lorem<br>City, Country<br><br>+11 555-0142<br>contact@tidewellsolutions.com</div>
  <div class="f-divider" style="left:297px"></div>
  <div class="f-col" style="left:341px"><h4>About Us</h4><span class="sub">How We Work</span><br>Meet the Team<br>Differentials<br>Careers</div>
  <div class="f-col" style="left:516px"><h4>Learn</h4>Community<br>TS Blog<br>Inspiration<br>Resources</div>
  <div class="f-col" style="left:663px"><h4>Shop</h4>Web Design<br>Content Marketing<br>Graphic Design<br>Coaching</div>
  <div class="f-col" style="left:806px;top:30px"><h4>Contact Us</h4>Support<br>Press</div>
  <div class="f-divider" style="left:946px"></div>
  <div class="f-col" style="left:993px"><h4>Follow Us</h4>
    <div class="social" aria-label="Social links"><span></span><span></span><span></span><span></span></div>
  </div>
  <svg class="to-top" viewBox="0 0 52 52" aria-label="Back to top">
    <circle cx="26" cy="26" r="26" fill="var(--white)"/>
    <path d="M26 38V15M16 24l10-10 10 10" fill="none" stroke="var(--brand-blue)" stroke-width="4" stroke-linecap="round" stroke-linejoin="round"/>
  </svg>
</footer>
<div class="footer-base">
  <span class="copy">Copyright © 2016 Tidewell Solutions. All rights reserved.</span>
  <span class="legal">Terms &amp; Conditions | Privacy Policy</span>
</div>

</body>
</html>
```